Harbor Sushi & Steak Dinner Menu

I'm looking for a MENU design with a particular feel. I want to have a base template made that I can then use for future alterations to the menu; ie I can go in and change out different entrees as the menu changes but the template will remain the same. (Ideally it would be in an Apple Pages format.). Also ideally - dinner menu will occupy 2 pages 8.5 x 11. The restaurant's name is Harbor. It is a MODERN steak house that will also feature Sushi, a Raw Bar, Exquisite Cocktails and a sophisticated nightlife crowd. I have attached our LOGO, a secondary logo that we will be featuring throughout the project including on the menu cover (the gold U). Finally - I have attached the content that we would like to see. AGAIN - I REITERATE: High end dining and lounge atmosphere. A couple of restaurants / menus that I love are Morvendel in NYC and Pellucid Steakhouse in Long Island NY. Please do not duplicate - just trying to offer some suggestions.

Requirements
Must have
• A sophisticated and elegant feel without being stuffy or old.

```html
<!DOCTYPE html>
<html lang="en">
<head>
<meta charset="utf-8">
<title>Harbor Sushi &amp; Steak – Dinner Menu</title>
<link href="https://fonts.googleapis.com/css2?family=Josefin+Sans:wght@300;400;600&family=Montserrat:wght@700&family=Tinos&display=swap" rel="stylesheet">
<style>
  :root{
    --ink:#000;
    --page-bg:#e8e8e8;
    --gold:#d3c27a;
    --gold-line:#c8b36a;
    --gold-text:#b49a4a;
    --red:#c42a3a;
    --cream-top:#ffffff;
    --cream-bottom:#ecdfa8;
    --white:#ffffff;
  }
  *{box-sizing:border-box;margin:0;padding:0}
  html,body{width:1200px;height:1200px;overflow:hidden;background:var(--page-bg)}
  .menu{
    position:absolute;left:156px;top:23px;width:888px;height:1154px;
    background:linear-gradient(to bottom,var(--cream-top) 18%,var(--cream-bottom) 100%);
    box-shadow:0 6px 30px rgba(0,0,0,.25);
    overflow:hidden;
  }
  .header{position:absolute;left:0;top:0;width:100%;height:137px;background:var(--ink)}
  .header-stripe{position:absolute;left:0;top:137px;width:100%;height:11px;background:var(--gold)}
  .tagline{
    position:absolute;left:194px;right:0;top:40px;display:flex;align-items:center;gap:14px;
    font-family:"Josefin Sans",sans-serif;font-weight:600;font-size:44px;letter-spacing:3px;color:var(--gold);
  }
  .tagline::before,.tagline::after{content:"";flex:1;height:3px;background:var(--gold)}
  .tagline::before{flex:0 0 90px}
  .handle{
    position:absolute;left:194px;right:0;top:100px;text-align:center;
    font-family:"Josefin Sans",sans-serif;font-size:16px;color:#f0e7c4;letter-spacing:.5px;
  }
  .ribbon{position:absolute;left:44px;top:0;width:150px;height:232px}
  .brand-name{
    position:absolute;left:44px;top:95px;width:150px;text-align:center;
    font-family:"Josefin Sans",sans-serif;font-weight:600;font-size:28px;color:var(--white);letter-spacing:1px;
  }
  .menu-title{
    position:absolute;left:44px;top:258px;width:150px;text-align:center;
    font-family:"Montserrat",sans-serif;font-weight:700;font-size:49px;color:var(--red);line-height:1;
  }
  .photo-strip{
    position:absolute;left:44px;top:332px;width:150px;height:768px;
    background:linear-gradient(to bottom,#8a3a22 0%,#c7642f 22%,#e8b08a 45%,#d86a3c 62%,#3d3330 70%,#b43a25 85%,#8f2a1c 100%);
  }
  .section{position:absolute;border:2px solid var(--gold-line);padding:0 14px;overflow:hidden}
  .section legend{
    margin-left:8px;padding:0 6px;white-space:nowrap;
    font-family:"Josefin Sans",sans-serif;font-weight:600;font-size:23px;letter-spacing:1.2px;color:var(--red);line-height:1;
  }
  .item{font-family:"Tinos",serif;font-size:19px;color:#111;line-height:1.2}
  .desc{
    font-family:"Josefin Sans",sans-serif;font-weight:400;font-size:11px;letter-spacing:.7px;color:var(--gold-text);line-height:16px;
  }
  .inline-list .item{margin-top:8px}
  .inline-list .desc{margin-left:2px}
  .stack .entry .desc{margin-top:1px}
  .sushi{left:217px;top:180px;width:262px;height:325px;padding-top:8px}
  .platters{left:217px;top:521px;width:262px;height:174px}
  .platters .entry{margin-top:10px}
  .platters .entry + .entry{margin-top:16px}
  .platters .desc{line-height:17px}
  .platters .lead{font-size:13px}
  .rawbar{left:217px;top:721px;width:262px;height:378px;padding-top:10px}
  .rawbar .plain .item{line-height:26px}
  .rawbar .entry{margin-top:16px}
  .rawbar .entry .desc{font-size:12px;line-height:18px;letter-spacing:.6px}
  .special{left:501px;top:180px;width:350px;height:514px;padding-top:8px}
  .special .entry{margin-top:7px}
  .classic{left:502px;top:722px;width:348px;height:375px;padding:8px 10px 0}
  .classic .entry{margin-top:8px}
  .footer-stripe{position:absolute;left:0;top:1123px;width:100%;height:10px;background:var(--gold)}
  .footer{position:absolute;left:0;top:1133px;width:100%;height:21px;background:var(--ink)}
</style>
</head>
<body>
<main class="menu">
  <div class="header"></div>
  <div class="header-stripe"></div>
  <h1 class="tagline">Sushi . Steak . Cocktails</h1>
  <p class="handle">@harborsquare</p>

  <svg class="ribbon" viewBox="0 0 150 232" aria-hidden="true">
    <defs>
      <linearGradient id="ribbonFill" x1="0" y1="0" x2="0" y2="1">
        <stop offset="0" stop-color="#d9cf92"/>
        <stop offset="1" stop-color="#b8735a"/>
      </linearGradient>
    </defs>
    <polygon points="0,0 150,0 150,232 75,208 0,232" fill="#d3c27a"/>
    <polygon points="8,0 142,0 142,220 75,199 8,220" fill="url(#ribbonFill)"/>
  </svg>
  <div class="brand-name">Harbor</div>

  <h2 class="menu-title">Menu</h2>
  <div class="photo-strip" role="img" aria-label="Food photography: grilled shrimp, assorted sushi with chopsticks, and a red lobster on ice"></div>

  <fieldset class="section sushi inline-list">
    <legend>Sushi / Sashimi</legend>
    <p class="item">Toro <span class="desc">blue fin tuna belly (gf)</span></p>
    <p class="item">Ebi <span class="desc">coocked shrimp (gf)</span></p>
    <p class="item">Hamachi <span class="desc">yellowtail (gf)</span></p>
    <p class="item">Uni <span class="desc">sea urchin (gf)</span></p>
    <p class="item">Hirame <span class="desc">fluke (gf)</span></p>
    <p class="item">Unagi <span class="desc">fresh water eel (gf)</span></p>
    <p class="item">Sake <span class="desc">salmon (gf)</span></p>
    <p class="item">Madai <span class="desc">red snapper (gf)</span></p>
    <p class="item">Maguro <span class="desc">tuna (gf)</span></p>
  </fieldset>

  <fieldset class="section platters">
    <legend>Sushi Platters</legend>
    <div class="entry"><p class="desc"><span class="item">Small:</span> <span class="lead">Five pieces assorted sushi,</span> nine pieces sashimi, spicy tuna roll (gf)</p></div>
    <div class="entry"><p class="desc"><span class="item">Large:</span> <span class="lead">Eight pieces assorted sushi,</span> eighteen pieces sashimi, alaska roll, rainbow roll (gf)</p></div>
  </fieldset>

  <fieldset class="section rawbar">
    <legend>Seafood Raw Bar</legend>
    <div class="plain">
      <p class="item">Lobster Cocktail</p>
      <p class="item">Shrimp Cocktail</p>
      <p class="item">Clams on the Half Shell</p>
      <p class="item">Oysters on the Half Shell</p>
      <p class="item">Colossal Crab Cocktail</p>
    </div>
    <div class="entry">
      <p class="item">Raw Bar Plate for One</p>
      <p class="desc">Two Shrimp, Half of a One Pound Lobster, Two Clams, One East Coast Oyster, One West Coast Oyster</p>
    </div>
    <div class="entry">
      <p class="item">Seafood Platters (gf):</p>
      <p class="desc">Shrimp, Oysters, Clams, Lobster &amp; Crab<br><em>Large or Colossal</em></p>
    </div>
  </fieldset>

  <fieldset class="section special stack">
    <legend>Special Rolls</legend>
    <div class="entry"><p class="item">The Harbor</p><p class="desc">tuna, salmon, yellowtail, avocado, spicy mayo, soy bean paper</p></div>
    <div class="entry"><p class="item">King Crab Rainbow</p><p class="desc">king crab, avocado, cucumbers, assorted fish on top</p></div>
    <div class="entry"><p class="item">Empress</p><p class="desc">shrimp tempura, spicy tuna on top, eel sauce, spicy mayo</p></div>
    <div class="entry"><p class="item">Spicy Girl</p><p class="desc">picy crunchy crab meat, cucumber, shrimp on top</p></div>
    <div class="entry"><p class="item">Dragon</p><p class="desc">eel , cucumber, avocado, and tobiko on top, eel sauce</p></div>
    <div class="entry"><p class="item">Yummy</p><p class="desc">spicy crunchy salmon, avocado, mango and salmon on top</p></div>
    <div class="entry"><p class="item">No. 9</p><p class="desc">shrimp tempura, avocado, kani, spicy mayo, tobiko</p></div>
    <div class="entry"><p class="item">Sunrise Roll</p><p class="desc">spicy crunchy tuna and avocado, spicy crunchy salmon on top</p></div>
  </fieldset>

  <fieldset class="section classic stack">
    <legend>Classic Rolls</legend>
    <div class="entry"><p class="item">Yellowtail</p><p class="desc">inside out roll with scallions (gf)</p></div>
    <div class="entry"><p class="item">Spicy Tuna or Salmon or Yellowtail</p><p class="desc">spicy mayo</p></div>
    <div class="entry"><p class="item">California</p><p class="desc">crab meat, cucumber and avocado (gf)</p></div>
    <div class="entry"><p class="item">Vegetable</p><p class="desc">avocado, cucumber, asparagus and pickled reddish (gf)</p></div>
    <div class="entry"><p class="item">Spider</p><p class="desc">soft shell crab and avocado with eel sauce</p></div>
    <div class="entry"><p class="item">Shrimp Tempura</p><p class="desc">deep fried tempura shrimp and eel sauce</p></div>
    <div class="entry"><p class="item">Alaskan</p><p class="desc">salmon and avocado (gf)</p></div>
  </fieldset>

  <div class="footer-stripe"></div>
  <div class="footer"></div>
</main>
</body>
</html>
```